Harbor Fieldworks (Business Card Design)

Need business cards designed. Something modern, chic, and sleek. Mabye the back of the card should be the navy blue that is in the logo and then just the logo on the back.

Target Market(s)

Those in the hotel, office, and renovation industry

Contact Information for Business Card

1. Logo 2. Dorian Velasko 3. CEO/Founder 4. Phone: (833) HarbFld / (833) 427-2353 5. Email: dorian@theharborfieldworks.com 6. Website: www.theharborfieldworks.com

Font styles to use
Other font styles liked:
• Look at the logo font and base the font for everything else off of that.

Colors
0054AA
0677BA
7BADD7
CADEEF
E8F1F8

Requirements
Must have
• Colors that are associated in the logo
Nice to have
• Sleek modern clean and chic design.

```html
<!DOCTYPE html>
<html lang="en">
<head>
<meta charset="utf-8">
<title>Harbor Fieldworks — Business Card</title>
<link rel="stylesheet" href="https://fonts.googleapis.com/css2?family=Montserrat:wght@600&family=Poppins:wght@300;400;700&display=swap">
<style>
  :root {
    --navy: #0c1a4b;
    --gold: #c89f3f;
    --ink: #1d1f2b;
    --paper: #ffffff;
    --backdrop: #ebebeb;
    --rule: #e2e2e2;
  }
  * { margin: 0; padding: 0; box-sizing: border-box; }
  html, body { width: 1200px; height: 2400px; overflow: hidden; }
  body {
    background: var(--backdrop);
    font-family: "Poppins", sans-serif;
    position: relative;
  }
  .card {
    position: absolute;
    left: 130px;
    width: 940px;
    height: 536px;
    box-shadow: 0 3px 8px rgba(0,0,0,0.28);
    overflow: hidden;
  }
  .card--front { top: 624px; background: var(--navy); }
  .card--back { top: 1240px; background: var(--paper); }

  .wordmark {
    position: absolute;
    left: 0; right: 0;
    display: flex;
    align-items: center;
    justify-content: center;
    gap: 18px;
    font-family: "Montserrat", sans-serif;
    font-weight: 600;
    letter-spacing: 4px;
    text-transform: uppercase;
  }
  .wordmark__square { width: 16px; height: 16px; background: var(--gold); }
  .card--front .wordmark { top: 236px; font-size: 44px; color: var(--paper); }
  .card--back .wordmark { top: 108px; font-size: 44px; color: var(--navy); }

  .front-rule {
    position: absolute; top: 446px; left: 130px; right: 0;
    height: 13px; background: var(--paper);
  }
  .front-square {
    position: absolute; top: 446px; left: 104px;
    width: 13px; height: 13px; background: var(--gold);
  }

  .person {
    position: absolute; left: 76px; top: 282px; width: 320px;
    text-align: center;
  }
  .person__name {
    font-weight: 700; font-size: 40px; color: var(--gold);
    line-height: 1.05; letter-spacing: 0.5px;
  }
  .person__title {
    font-weight: 300; font-size: 27px; color: var(--ink); line-height: 1.2;
  }
  .divider {
    position: absolute; left: 430px; top: 262px;
    width: 2px; height: 126px; background: var(--rule);
  }
  .contact { position: absolute; left: 460px; top: 264px; list-style: none; }
  .contact__item {
    display: flex; align-items: center; gap: 12px;
    height: 42px;
    font-size: 22px; color: var(--ink);
  }
  .contact__item svg { width: 22px; height: 22px; flex: none; }

  .back-rule {
    position: absolute; top: 461px; left: 0; width: 845px;
    height: 12px; background: var(--navy);
  }
  .back-square {
    position: absolute; top: 461px; left: 858px;
    width: 12px; height: 12px; background: var(--gold);
  }
</style>
</head>
<body>
  <section class="card card--front" aria-label="Card front">
    <div class="wordmark"><span class="wordmark__square"></span>Harbor Fieldworks</div>
    <span class="front-square"></span>
    <span class="front-rule"></span>
  </section>

  <section class="card card--back" aria-label="Card back">
    <div class="wordmark"><span class="wordmark__square"></span>Harbor Fieldworks</div>

    <div class="person">
      <p class="person__name">DORIAN VELASKO</p>
      <p class="person__title">CEO/FOUNDER</p>
    </div>
    <span class="divider"></span>

    <ul class="contact">
      <li class="contact__item">
        <svg viewBox="0 0 24 24" aria-hidden="true"><path fill="var(--gold)" d="M6.6 10.8a15.1 15.1 0 0 0 6.6 6.6l2.2-2.2a1 1 0 0 1 1-.25 11.4 11.4 0 0 0 3.6.57 1 1 0 0 1 1 1V20a1 1 0 0 1-1 1A17 17 0 0 1 3 4a1 1 0 0 1 1-1h3.5a1 1 0 0 1 1 1c0 1.25.2 2.45.57 3.57a1 1 0 0 1-.25 1z"/></svg>
        (833) HarbFld / (833) 427-2353
      </li>
      <li class="contact__item">
        <svg viewBox="0 0 24 24" aria-hidden="true"><rect x="2" y="5" width="20" height="14" fill="var(--gold)"/><path d="M2.5 5.5 12 13l9.5-7.5" fill="none" stroke="#fff" stroke-width="1.6"/></svg>
        dorian@theharborfieldworks.com
      </li>
      <li class="contact__item">
        <svg viewBox="0 0 24 24" aria-hidden="true"><g fill="none" stroke="var(--gold)" stroke-width="2"><circle cx="12" cy="12" r="9"/><ellipse cx="12" cy="12" rx="4" ry="9"/><path d="M3 12h18M5 7h14M5 17h14"/></g></svg>
        www.theharborfieldworks.com
      </li>
    </ul>

    <span class="back-rule"></span>
    <span class="back-square"></span>
  </section>
</body>
</html>
```